A clean crisp business card for a Landscape Construction company. Designed to be easy to read contact/ info and also be appealing/interesting, unlike a traditional business card.

Industry/Entity Type

Landscape Construction

Contact Information for Business Card

Company name : Bramblecrest Landscape Construction, phone number: (877) 62Vales, website:Bramblecrestlandscapes.example, Email, sales@bramblecrestlandscapes.example

Requirements
Nice to have
• Luxurious finishes/ details…. Icons or emblems next to contact info
Should not have
• Clipart or general pictures

```html
<!DOCTYPE html>
<html lang="en">
<head>
<meta charset="utf-8">
<title>Bramblecrest Landscape Construction – Business Card</title>
<link rel="stylesheet" href="https://fonts.googleapis.com/css2?family=Cinzel:wght@400;600&family=Raleway:wght@400&display=swap">
<style>
  :root {
    --page-bg: #e4e5e7;
    --card-white: #ffffff;
    --royal-blue: #1d2fb8;
    --deep-blue: #14209a;
    --bright-blue: #2f4fd6;
    --leaf-green: #4fd22a;
    --lime-green: #8fc93a;
    --brand-blue: #2457b0;
    --brand-green: #7cb83a;
    --text-light: #ffffff;
  }
  * { margin: 0; padding: 0; box-sizing: border-box; }
  html, body { width: 1200px; height: 794px; overflow: hidden; }
  body {
    background: var(--page-bg);
    display: flex;
    flex-direction: column;
    align-items: center;
    justify-content: center;
    gap: 30px;
  }
  .card {
    position: relative;
    width: 620px;
    height: 354px;
    overflow: hidden;
    box-shadow: 0 6px 18px rgba(0,0,0,0.18);
  }
  .card-front { background: var(--card-white); }
  .card-back { background: linear-gradient(160deg, var(--bright-blue), var(--deep-blue)); }
  .card-art { position: absolute; inset: 0; width: 100%; height: 100%; }

  .brand {
    position: absolute;
    left: 70px;
    top: 58px;
    width: 290px;
    text-align: center;
  }
  .brand-dot {
    display: block;
    width: 34px; height: 34px;
    margin: 0 auto 12px;
    border-radius: 50%;
    background: var(--brand-green);
  }
  .brand-name {
    font-family: "Cinzel", serif;
    font-weight: 600;
    font-size: 33px;
    color: var(--brand-blue);
    line-height: 1;
  }
  .brand-tagline {
    font-family: "Cinzel", serif;
    font-weight: 400;
    font-size: 12.5px;
    letter-spacing: 1.6px;
    color: var(--brand-green);
    margin-top: 5px;
  }

  .contact-list {
    position: absolute;
    left: 40px;
    top: 36px;
    list-style: none;
    font-family: "Raleway", sans-serif;
    font-size: 16px;
    color: var(--text-light);
  }
  .contact-item {
    display: flex;
    align-items: center;
    gap: 14px;
    margin-bottom: 10px;
  }
  .contact-icon { width: 16px; height: 16px; flex: none; }
</style>
</head>
<body>

  <section class="card card-back" aria-label="Card back with contact details">
    <svg class="card-art" viewBox="0 0 620 354" preserveAspectRatio="none" aria-hidden="true">
      <path d="M0,250 C150,300 330,320 460,300 C540,288 590,290 620,300 L620,354 L0,354 Z" fill="var(--card-white)"/>
      <path d="M0,262 C150,312 330,330 460,312 C540,300 590,302 620,312 L620,354 L0,354 Z" fill="var(--lime-green)"/>
      <path d="M0,280 C150,326 330,342 470,326 C545,318 595,320 620,328 L620,354 L0,354 Z" fill="var(--leaf-green)"/>
      <path d="M0,300 C160,344 340,352 620,342 L620,354 L0,354 Z" fill="var(--royal-blue)"/>
    </svg>
    <ul class="contact-list">
      <li class="contact-item">
        <svg class="contact-icon" viewBox="0 0 16 16" aria-hidden="true"><path fill="currentColor" d="M3.5 1.5l2.2 0 1 3.2-1.5 1.2c.9 1.9 2.2 3.2 4 4l1.2-1.5 3.2 1v2.2c0 .8-.7 1.4-1.5 1.4C6.6 13 3 9.4 2.1 3c0-.8.6-1.5 1.4-1.5z"/></svg>
        <span>(877) 62Vales</span>
      </li>
      <li class="contact-item">
        <svg class="contact-icon" viewBox="0 0 16 16" aria-hidden="true"><rect x="1" y="3" width="14" height="10" rx="1" fill="currentColor"/><path d="M1.5 3.5L8 9l6.5-5.5" fill="none" stroke="var(--royal-blue)" stroke-width="1.3"/></svg>
        <span>sales@bramblecrestlandscapes.example</span>
      </li>
      <li class="contact-item">
        <svg class="contact-icon" viewBox="0 0 16 16" aria-hidden="true"><circle cx="8" cy="8" r="6.5" fill="none" stroke="currentColor" stroke-width="1.4"/><ellipse cx="8" cy="8" rx="2.8" ry="6.5" fill="none" stroke="currentColor" stroke-width="1.2"/><path d="M1.5 8h13" stroke="currentColor" stroke-width="1.2"/></svg>
        <span>Bramblecrestlandscapes.example</span>
      </li>
    </ul>
  </section>

  <section class="card card-front" aria-label="Card front with company name">
    <svg class="card-art" viewBox="0 0 620 354" preserveAspectRatio="none" aria-hidden="true">
      <defs>
        <linearGradient id="front-blue" x1="0" y1="0" x2="1" y2="1">
          <stop offset="0" stop-color="var(--bright-blue)"/>
          <stop offset="1" stop-color="var(--deep-blue)"/>
        </linearGradient>
      </defs>
      <path d="M0,232 C160,300 300,240 390,150 C470,80 560,62 620,66 L620,354 L0,354 Z" fill="var(--lime-green)"/>
      <path d="M0,262 C160,322 300,262 395,172 C475,100 560,84 620,88 L620,354 L0,354 Z" fill="var(--leaf-green)"/>
      <path d="M0,300 C170,350 320,285 410,195 C490,124 565,112 620,116 L620,354 L0,354 Z" fill="var(--card-white)"/>
      <path d="M0,312 C170,362 330,295 420,205 C500,134 570,122 620,126 L620,354 L0,354 Z" fill="url(#front-blue)"/>
      <circle cx="520" cy="270" r="62" fill="var(--card-white)" opacity="0.18"/>
    </svg>
    <div class="brand">
      <span class="brand-dot"></span>
      <div class="brand-name">Bramblecrest</div>
      <div class="brand-tagline">LANDSCAPE CONSTRUCTION</div>
    </div>
  </section>

</body>
</html>
```